I need a business card representing my company, VELDAR, it's an artist management and design company. Complete name is "VELDAR Artist Mgmt. + Design Co." I need it to be world class and very appealing, sophisticated and artistically unique.
Updates

Posted an updated Brief please see. I need a business card representing my company, VELDAR, it's an artist management and design company. Complete name is "VELDAR Artist Mgmt. + Design Co." I need it to be world class and very appealing, sophisticated and artistically unique.

Designs look the same

Designs look the same

Target Market(s)

Advertisers, Entertainment Companies, Commercial companies

Industry/Entity Type

Advertising

Contact Information for Business Card

I need a business card representing my company, VELDAR, it's an artist management and design company. Complete name is "VELDAR Artist Mgmt. + Design Co." I need it to be world class and very appealing, sophisticated and artistically unique. One side can be VELDAR Artist Mgmt. + Design Co. and the other my name, Theodore Quillan, my contact telephone: 415.638.2097, email veldarartist@mailnest.example, my address: 2416 Harrowgate Ave. #317 Miami, FL 33152

Font styles to use
Other font styles liked:
• Calibri

Colors
ffffff
0455a3
f37122

Requirements
Must have
• "VELDAR" stand out bigger than the rest of the text.
Nice to have
• Name "VELDAR" can be centered on one side or in the corner or along side edges, just need something cool and different.
Should not have
• I am open just try to keep it clean looking

```html
<!DOCTYPE html>
<html lang="en">
<head>
<meta charset="utf-8">
<title>VELDAR Business Card</title>
<link rel="stylesheet" href="https://fonts.googleapis.com/css2?family=Ropa+Sans&family=Saira+Semi+Condensed:wght@500;700&display=swap">
<style>
  :root {
    --backdrop: #1c1c1c;
    --card: #ffffff;
    --brand-blue: #0455a3;
    --brand-orange: #f37122;
    --ink: #222222;
    --dot-field: #ececec;
  }
  * { margin: 0; padding: 0; box-sizing: border-box; }
  html, body {
    width: 1200px;
    height: 1000px;
    overflow: hidden;
    background: var(--backdrop);
  }
  .canvas {
    position: relative;
    width: 1200px;
    height: 1000px;
  }
  .card {
    position: absolute;
    left: 250px;
    width: 700px;
    height: 400px;
    background: var(--card);
    border-radius: 28px;
    overflow: hidden;
  }
  .card--front { top: 80px; }
  .card--back { top: 520px; }

  .front-art {
    position: absolute;
    inset: 0;
  }
  .brand {
    position: absolute;
    left: 150px;
    top: 118px;
    color: var(--ink);
  }
  .brand__name {
    font-family: "Saira Semi Condensed", sans-serif;
    font-weight: 700;
    font-size: 118px;
    line-height: 1;
    letter-spacing: 2px;
  }
  .brand__tagline {
    margin-top: 4px;
    padding-left: 8px;
    font-family: "Ropa Sans", sans-serif;
    font-size: 24px;
    letter-spacing: 0.5px;
  }

  .accent-bar {
    position: absolute;
    width: 9px;
  }
  .accent-bar--blue {
    left: 28px;
    top: 0;
    height: 72px;
    background: var(--brand-blue);
  }
  .accent-bar--orange {
    left: 300px;
    top: 228px;
    height: 172px;
    background: var(--brand-orange);
  }
  .holder-name {
    position: absolute;
    left: 62px;
    top: 34px;
    font-family: "Saira Semi Condensed", sans-serif;
    font-weight: 700;
    font-size: 38px;
    color: var(--ink);
  }
  .contact {
    position: absolute;
    left: 336px;
    top: 250px;
    font-family: "Ropa Sans", sans-serif;
    font-size: 24px;
    line-height: 1.3;
    color: var(--ink);
    font-style: normal;
  }
  .contact__group + .contact__group { margin-top: 12px; }
</style>
</head>
<body>
<main class="canvas">

  <section class="card card--front" aria-label="Card front">
    <svg class="front-art" width="700" height="400" viewBox="0 0 700 400">
      <defs>
        <clipPath id="disc-left">
          <polygon points="0,0 300,0 150,400 0,400"/>
        </clipPath>
        <clipPath id="disc-right">
          <polygon points="300,0 700,0 700,400 150,400"/>
        </clipPath>
      </defs>
      <circle cx="300" cy="210" r="270" fill="var(--brand-orange)" clip-path="url(#disc-left)"/>
      <circle cx="300" cy="210" r="270" fill="var(--dot-field)" clip-path="url(#disc-right)"
              role="img" aria-label="Halftone dot pattern filling the right half of the disc"/>
    </svg>
    <div class="brand">
      <div class="brand__name">VELDAR</div>
      <div class="brand__tagline">Artist Mgmt. + Design Co.</div>
    </div>
  </section>

  <section class="card card--back" aria-label="Card back">
    <span class="accent-bar accent-bar--blue"></span>
    <h1 class="holder-name">Theodore Quillan</h1>
    <span class="accent-bar accent-bar--orange"></span>
    <address class="contact">
      <div class="contact__group">
        <div>415.638.2097</div>
        <div>veldarartist@mailnest.example</div>
      </div>
      <div class="contact__group">
        <div>2416 Harrowgate Ave.</div>
        <div>#317 Miami, FL 33152</div>
      </div>
    </address>
  </section>

</main>
</body>
</html>
```